I am medical doctor in surgery specialized in Urology and anti-aging. I need Web and Instagram design for a head cream , face cream and body lotion. I did a 2% GHK-Cu solution (head-face-body) with an professional pharmacist specialized in manufacturing creams. . GHK-Cu is a tri-peptide with solid scientific background to rejuvenate the skin (will stimulate collagen production) and can promote hair regrowth. Statistically 70% of peptides bought are fake on the market, I can personally guarantee about purity (my peptides are certified pure above 99% checked in an independent laboratory in London -UK.
I want to use the name 'Lunavel'. I secured already the domain names. I had an design for another project I could re-use for this project. The ribbon should include more blue. The font of Lunavel can be changed. I got a logo which is ok for me. Web design best coded with Wordpress.

Target Market(s)

Anti aging, skin care, hair regrowth, skin collagen

Industry/Entity Type

the cream can also be used after surgery for faster and better wound healing

Number of Pages Required

5+ page

Font styles to use
Sans Serif

Colors
0054AA
0677BA
7BADD7
CADEEF
E8F1F8

Requirements
Must have
• target population 30-70 years
Nice to have
• scientific proof, pictures before-after
Should not have
• GHK-Cu has solid scientific animal studies of anti-cancer properties. It is 100% safe for dermal human use.

```html
<!DOCTYPE html>
<html lang="en">
<head>
<meta charset="utf-8">
<title>Lunavel — Premium GHK-Cu Peptides</title>
<link href="https://fonts.googleapis.com/css2?family=Inter:wght@400;500;600;700&display=swap" rel="stylesheet">
<style>
:root{
  --primary:#0054AA;
  --secondary:#0677BA;
  --sky:#7BADD7;
  --mist:#CADEEF;
  --pale:#E8F1F8;
  --bg:#F3F8FD;
  --band:#EAF2FA;
  --ink:#0B3F86;
  --text:#3F4854;
  --muted:#5C6673;
  --white:#FFFFFF;
}
*{box-sizing:border-box;margin:0;padding:0}
html,body{width:1200px;height:3785px;overflow:hidden}
body{font-family:'Inter',sans-serif;background:var(--bg);color:var(--text);position:relative}
.nav{height:68px;display:flex;align-items:center;padding:0 23px;border-bottom:1px solid var(--pale);background:var(--bg)}
.brand{font-weight:700;font-size:27px;color:var(--primary);letter-spacing:-.5px}
.nav-links{display:flex;gap:30px;margin-left:46px;font-size:12px;color:var(--text)}
.btn-shop{margin-left:auto;background:var(--primary);color:#fff;font-size:12px;font-weight:600;padding:10px 23px;border-radius:3px}
.hero{position:absolute;top:68px;left:0;width:1200px;height:794px}
.pill{position:absolute;left:23px;top:222px;background:var(--mist);color:var(--primary);font-size:11px;font-weight:600;padding:7px 15px;border-radius:14px;letter-spacing:.3px}
.hero h1{position:absolute;left:22px;top:280px;font-size:42px;line-height:56px;font-weight:500;color:var(--ink);letter-spacing:-.6px}
.hero h1 span{color:var(--primary)}
.hero p{position:absolute;left:23px;top:420px;width:380px;font-size:17px;line-height:26px;color:var(--text)}
.btn-main{position:absolute;left:23px;top:544px;width:194px;height:52px;background:var(--primary);color:#fff;font-size:14px;font-weight:600;display:flex;align-items:center;justify-content:center;border-radius:3px;box-shadow:0 6px 14px rgba(0,84,170,.25)}
.btn-link{position:absolute;left:240px;top:560px;display:flex;align-items:center;gap:7px;font-size:15px;font-weight:600;color:var(--primary)}
.hero-photo{position:absolute;left:630px;top:127px;width:547px;height:562px;border-radius:18px;background:linear-gradient(180deg,#d9dfe6 0%,#c3ccd6 68%,#e8ecf0 70%,#dfe4ea 100%);box-shadow:0 14px 34px rgba(11,63,134,.18)}
.trust{position:absolute;top:862px;left:0;width:1200px;height:112px;background:var(--band);display:flex;align-items:center;justify-content:space-between;padding:0 23px}
.trust-item{display:flex;align-items:center;gap:10px;font-size:12px;font-weight:600;letter-spacing:1.2px;color:var(--muted)}
.peptide{position:absolute;top:974px;left:0;width:1200px;height:674px;background:var(--bg)}
.peptide h2{position:absolute;left:22px;top:115px;width:460px;font-size:29px;line-height:38px;font-weight:500;color:var(--ink)}
.peptide .lead{position:absolute;left:23px;top:222px;width:455px;font-size:17px;line-height:26px}
.results{position:absolute;left:23px;top:322px;height:164px;border-left:4px solid var(--primary);padding:18px 0 0 23px}
.results h3{font-size:15px;font-weight:600;color:var(--ink);margin-bottom:14px}
.results li{list-style:none;font-size:15px;line-height:34px;display:flex;gap:8px;align-items:flex-start}
.results li svg{margin-top:6px;flex:none}
.rule{position:absolute;left:23px;top:510px;width:447px;border-top:1px solid var(--mist)}
.note{position:absolute;left:23px;top:528px;width:455px;font-size:12.5px;line-height:19px;color:var(--muted)}
.ph-mol{position:absolute;left:529px;top:213px;width:316px;height:300px;border-radius:4px;background:radial-gradient(circle at 50% 50%,#f7fafd,#dfe6ee);box-shadow:0 8px 20px rgba(11,63,134,.12)}
.ph-skin{position:absolute;left:861px;top:167px;width:316px;height:299px;border-radius:4px;background:linear-gradient(160deg,#b9d0e6 0%,#e4ebf3 40%,#c9d5e2 85%,#7ea7cf 100%);box-shadow:0 8px 20px rgba(11,63,134,.12)}
.collection{position:absolute;top:1648px;left:0;width:1200px;height:967px;background:var(--band)}
.eyebrow{font-size:11.5px;font-weight:600;letter-spacing:2.2px;color:var(--primary)}
.collection .eyebrow{position:absolute;left:23px;top:118px}
.collection h2{position:absolute;left:22px;top:153px;font-size:29px;font-weight:500;color:var(--ink)}
.view-all{position:absolute;right:23px;top:174px;display:flex;align-items:center;gap:6px;font-size:12px;font-weight:600;color:var(--primary)}
.card{position:absolute;top:250px;width:363px;height:602px;background:#fff;border-radius:3px;box-shadow:0 2px 8px rgba(11,63,134,.06)}
.card-photo{height:363px;position:relative}
.card-body{padding:30px 30px 0}
.card h3{font-size:22px;font-weight:500;color:var(--ink);margin-bottom:14px}
.card p{font-size:14.5px;line-height:22.5px;color:var(--muted)}
.card-foot{position:absolute;left:30px;right:30px;bottom:30px;display:flex;justify-content:space-between;align-items:center}
.price{font-size:14px;font-weight:600;color:var(--ink)}
.cart{width:38px;height:38px;border-radius:5px;background:var(--primary);display:flex;align-items:center;justify-content:center}
.tag{position:absolute;right:16px;top:16px;background:var(--ink);color:#fff;font-size:11px;font-weight:600;padding:5px 12px;border-radius:11px}
.founder{position:absolute;top:2615px;left:0;width:1200px;height:649px;background:var(--bg)}
.ph-founder{position:absolute;left:23px;top:178px;width:540px;height:292px;border-radius:8px;background:linear-gradient(90deg,#9a9a9a,#d6d6d6 45%,#8c8c8c);box-shadow:0 10px 24px rgba(0,0,0,.18)}
.founder .eyebrow{position:absolute;left:638px;top:123px}
.founder h2{position:absolute;left:637px;top:151px;width:540px;font-size:29px;line-height:38px;font-weight:500;color:var(--ink)}
.founder .lead{position:absolute;left:638px;top:250px;width:540px;font-size:17px;line-height:26px}
.quote{position:absolute;left:638px;top:350px;width:539px;border-left:3px solid var(--sky);padding:0 0 0 32px;font-size:15.5px;line-height:23px;color:var(--primary)}
.stats{position:absolute;left:638px;top:495px;display:flex;gap:0}
.stat{width:285px;font-size:15px;line-height:22px}
.stat b{display:block;font-weight:600;color:var(--ink);font-size:14px}
.footer{position:absolute;top:3264px;left:0;width:1200px;height:521px;background:#fff}
.footer .brand{position:absolute;left:23px;top:123px;font-size:22px;font-weight:600}
.f-about{position:absolute;left:23px;top:172px;width:265px;font-size:15px;line-height:22.5px;color:var(--muted)}
.f-icons{position:absolute;left:23px;top:289px;display:flex;gap:14px}
.f-col{position:absolute;top:116px}
.f-col h4{font-size:11.5px;font-weight:700;letter-spacing:.6px;color:var(--text);margin-bottom:28px}
.f-col a{display:block;font-size:15px;color:var(--muted);text-decoration:none;margin-bottom:16px}
.copy{position:absolute;left:0;width:1200px;top:392px;text-align:center;font-size:11.5px;font-weight:500;color:var(--text)}
</style>
</head>
<body>
<header class="nav">
  <div class="brand">Lunavel</div>
  <nav class="nav-links"><span>Hair</span><span>Face</span><span>Body</span><span>Science</span><span>About</span></nav>
  <div class="btn-shop">Shop Now</div>
</header>

<section class="hero">
  <div class="pill">PREMIUM GHK-CU PEPTIDES</div>
  <h1>The Science of Purity.<br><span>The Art of Rejuvenation.</span></h1>
  <p>Developed by specialized surgeons and pharmacists. 99.9% Purity Certified GHK-Cu solution for cellular skin restoration.</p>
  <div class="btn-main">Explore the Science</div>
  <div class="btn-link"><svg width="16" height="16" viewBox="0 0 16 16" fill="none" stroke="currentColor" stroke-width="1.5"><path d="M5.5 1.5h5M6.5 1.5v5L2 14.5h12L9.5 6.5v-5"/></svg>Clinical Studies</div>
  <div class="hero-photo" role="img" aria-label="Blue dropper bottle of clinical peptide serum on a white laboratory bench"></div>
</section>

<section class="trust">
  <div class="trust-item"><svg width="18" height="18" viewBox="0 0 18 18" fill="none" stroke="#0054AA" stroke-width="1.4"><circle cx="9" cy="9" r="7.5"/><path d="M5.5 9.2l2.3 2.3 4.7-4.9"/></svg>99% CERTIFIED PURE</div>
  <div class="trust-item"><svg width="18" height="18" viewBox="0 0 18 18" fill="none" stroke="#0054AA" stroke-width="1.4"><rect x="2" y="4.5" width="14" height="11.5" rx="1.5"/><path d="M6.5 4.5V2.5h5v2M9 7.5v5M6.5 10h5"/></svg>SURGEON FORMULATED</div>
  <div class="trust-item"><svg width="18" height="18" viewBox="0 0 18 18" fill="none" stroke="#0054AA" stroke-width="1.4"><path d="M7 2l4 6M5.5 3.5l2-1.2M3 16h12M9 16a5 5 0 0 0 4-7"/><circle cx="9" cy="11" r="1.5"/></svg>PHARMACIST MANUFACTURED</div>
  <div class="trust-item"><svg width="18" height="18" viewBox="0 0 18 18" fill="none" stroke="#0054AA" stroke-width="1.4"><rect x="2.5" y="2" width="10" height="14" rx="1"/><path d="M5 6h5M5 9h5M5 12h2.5"/><path d="M11.5 13.5l1.5 1.5 3-3"/></svg>CLINICALLY PROVEN</div>
</section>

<section class="peptide">
  <h2>The Tri-Peptide Revolution: GHK-Cu</h2>
  <p class="lead">GHK-Cu is a naturally occurring copper complex that naturally declines as we age. Our formula restores this vital molecule at a surgical-grade 99.9% concentration.</p>
  <div class="results">
    <h3>Clinical Results</h3>
    <ul>
      <li><svg width="12" height="12" viewBox="0 0 12 12" fill="none" stroke="#7BADD7" stroke-width="1.2"><circle cx="6" cy="6" r="5"/><path d="M3.8 6.1l1.6 1.5 2.8-3"/></svg>Dynamic collagen stimulation for dermal density</li>
      <li><svg width="12" height="12" viewBox="0 0 12 12" fill="none" stroke="#7BADD7" stroke-width="1.2"><circle cx="6" cy="6" r="5"/><path d="M3.8 6.1l1.6 1.5 2.8-3"/></svg>Follicle activation for accelerated hair growth</li>
      <li><svg width="12" height="12" viewBox="0 0 12 12" fill="none" stroke="#7BADD7" stroke-width="1.2"><circle cx="6" cy="6" r="5"/><path d="M3.8 6.1l1.6 1.5 2.8-3"/></svg>Enhanced wound healing and tissue repair protocols</li>
    </ul>
  </div>
  <div class="rule"></div>
  <p class="note">*All batches are independently certified for purity and concentration by a premier independent laboratory in London, UK.</p>
  <div class="ph-mol" role="img" aria-label="Illustration of a GHK-Cu molecule with a central copper atom"></div>
  <div class="ph-skin" role="img" aria-label="Close-up of smooth skin texture in cool blue light"></div>
</section>

<section class="collection">
  <div class="eyebrow">THE CLINICAL COLLECTION</div>
  <h2>Advanced Delivery Systems</h2>
  <div class="view-all">View All Products <svg width="16" height="14" viewBox="0 0 16 14" fill="none" stroke="currentColor" stroke-width="1.5"><path d="M1 7h13M9 2l5 5-5 5"/></svg></div>

  <article class="card" style="left:23px">
    <div class="card-photo" role="img" aria-label="Silver jar of face rejuvenation cream on white marble" style="background:linear-gradient(180deg,#e6e8ea,#c9cdd1 60%,#dcdfe2)"><span class="tag">Best Seller</span></div>
    <div class="card-body"><h3>Face Rejuvenation Cream</h3><p>Intensive dermal repair with high-potency copper peptides for deep-line reduction.</p></div>
    <div class="card-foot" style="bottom:53px"><span class="price">£145.00</span><span class="cart"><svg width="18" height="18" viewBox="0 0 18 18" fill="none" stroke="#fff" stroke-width="1.5"><path d="M1.5 2h2.5l2 9h8l2-6H5M9 5v3.5M7.3 6.8h3.5"/><circle cx="7" cy="14.5" r="1.2"/><circle cx="13" cy="14.5" r="1.2"/></svg></span></div>
  </article>

  <article class="card" style="left:419px">
    <div class="card-photo" role="img" aria-label="Amber dropper bottle of head and hair growth serum on a tiled counter" style="background:linear-gradient(180deg,#e1e6ea,#cfd6dc 70%,#9fa8b0)"></div>
    <div class="card-body"><h3>Head &amp; Hair Growth Serum</h3><p>Follicle-stimulating GHK-Cu solution designed to reverse thinning and enhance scalp health.</p></div>
    <div class="card-foot"><span class="price">£180.00</span><span class="cart"><svg width="18" height="18" viewBox="0 0 18 18" fill="none" stroke="#fff" stroke-width="1.5"><path d="M1.5 2h2.5l2 9h8l2-6H5M9 5v3.5M7.3 6.8h3.5"/><circle cx="7" cy="14.5" r="1.2"/><circle cx="13" cy="14.5" r="1.2"/></svg></span></div>
  </article>

  <article class="card" style="left:814px">
    <div class="card-photo" role="img" aria-label="White pump bottle of total body therapy lotion on a stone counter" style="background:linear-gradient(180deg,#ebebe9,#d6d3cf 70%,#c0bbb4)"></div>
    <div class="card-body"><h3>Total Body Therapy Lotion</h3><p>Full-body cellular repair for post-surgical recovery and environmental damage reversal.</p></div>
    <div class="card-foot"><span class="price">£110.00</span><span class="cart"><svg width="18" height="18" viewBox="0 0 18 18" fill="none" stroke="#fff" stroke-width="1.5"><path d="M1.5 2h2.5l2 9h8l2-6H5M9 5v3.5M7.3 6.8h3.5"/><circle cx="7" cy="14.5" r="1.2"/><circle cx="13" cy="14.5" r="1.2"/></svg></span></div>
  </article>
</section>

<section class="founder">
  <div class="ph-founder" role="img" aria-label="Black and white portrait of the founding surgeon in a white coat in his office"></div>
  <div class="eyebrow">THE VISIONARY</div>
  <h2>Formulated by Surgeons, Driven by Results</h2>
  <p class="lead">Lunavel was founded by a leading Consultant Surgeon with a distinguished background in Urology and specialized Anti-aging procedures.</p>
  <blockquote class="quote">"In surgery, precision is everything. I applied that same philosophy to skincare—removing the filler, the noise, and focusing entirely on the pharmaceutical purity of GHK-Cu."</blockquote>
  <div class="stats">
    <div class="stat"><b>20+ Years</b>Surgical Experience</div>
    <div class="stat"><b>10,000+</b>Clinical Procedures</div>
  </div>
</section>

<footer class="footer">
  <div class="brand">Lunavel</div>
  <p class="f-about">Advanced GHK-Cu skincare solutions bridging the gap between clinical surgery and daily rejuvenation.</p>
  <div class="f-icons">
    <svg width="18" height="18" viewBox="0 0 18 18" fill="none" stroke="#0054AA" stroke-width="1.5"><circle cx="9" cy="9" r="7.5"/><path d="M1.5 9h15M9 1.5c2.5 2.5 2.5 12.5 0 15M9 1.5c-2.5 2.5-2.5 12.5 0 15"/></svg>
    <svg width="18" height="18" viewBox="0 0 18 18" fill="none" stroke="#0054AA" stroke-width="1.5"><path d="M2 7v4h3l4 3V4L5 7zM12 6.5l3-1.5M12 9h3.5M12 11.5l3 1.5"/></svg>
    <svg width="18" height="18" viewBox="0 0 18 18" fill="none" stroke="#0054AA" stroke-width="1.5"><path d="M4 1.5h7l3 3v12H4z"/><path d="M7 10.5l1.5 1.5 3-3"/></svg>
  </div>
  <div class="f-col" style="left:323px"><h4>TREATMENTS</h4><a>Hair Care</a><a>Face Rejuvenation</a><a>Body Therapy</a></div>
  <div class="f-col" style="left:623px"><h4>RESEARCH</h4><a>The Science</a><a>Clinical Studies</a><a>Founder's Story</a></div>
  <div class="f-col" style="left:923px"><h4>LEGAL</h4><a>Privacy Policy</a><a>Terms of Service</a><a>Shipping</a></div>
  <p class="copy">© 2024 Lunavel Medical Grade Skincare. Developed by Clinical Scientists.</p>
</footer>
</body>
</html>
```